Coastal Bright Sweep Business Card

We are a cleaning and waste management company with the slogan "Turning everyday waste into a fresh new start". We would like a re-design of our current business card. On the front we want to continue to use our logo as the focus point. On the back, we want the whole thing re-done to be less busy. We want the staff member’s name, the job title, mobile number, email and website. We do not want the address on the card. We still want the green, black and blue colours used, but a new font for the information on the back. Please do not change the logo design at all. We are also thinking about using icons to replace the text ‘mobile, email, website’. The “events + commercial” banner needs to be incorporated somewhere and needs to read “events + commercial + waste”. Another important point for consideration is that we are very concerned about being environmentally sustainable and will be printing on recycled paper. All designs should be made to compliment this in regards to boldness and colouring. Please find attached our logo, our colour chart and an image of our current business card.

```html
<!DOCTYPE html>
<html lang="en">
<head>
<meta charset="utf-8">
<title>Coastal Bright Sweep Business Card</title>
<link rel="stylesheet" href="https://fonts.googleapis.com/css2?family=Open+Sans:ital,wght@0,400;0,700;1,600;1,700&family=Roboto+Slab:wght@700&display=swap">
<style>
  :root {
    --backdrop: #dcd8d2;
    --paper: #f1efea;
    --paper-edge: #1d3a6e;
    --green: #7aae2e;
    --teal: #1a9fb3;
    --navy: #1d3a6e;
    --ink: #3a3d42;
  }
  * { margin: 0; padding: 0; box-sizing: border-box; }
  html, body {
    width: 1200px;
    height: 918px;
    overflow: hidden;
    background: var(--backdrop);
  }
  .sheet {
    width: 1200px;
    height: 918px;
    display: flex;
    flex-direction: column;
    align-items: center;
    justify-content: center;
    gap: 44px;
  }
  .card {
    position: relative;
    width: 620px;
    height: 378px;
    background: var(--paper);
    border-bottom: 4px solid var(--paper-edge);
    box-shadow: 0 2px 6px rgba(0, 0, 0, 0.12);
    font-family: "Open Sans", Arial, sans-serif;
  }

  /* Front */
  .card--front .brand-name {
    position: absolute;
    left: 70px;
    top: 110px;
    font-size: 44px;
    font-weight: 700;
    color: var(--green);
    letter-spacing: -0.5px;
    white-space: nowrap;
  }
  .card--front .slogan {
    position: absolute;
    right: 70px;
    top: 178px;
    font-size: 16px;
    font-style: italic;
    font-weight: 600;
    color: var(--ink);
    white-space: nowrap;
  }
  .card--front .services {
    position: absolute;
    left: 70px;
    top: 262px;
    font-size: 18px;
    font-style: italic;
    font-weight: 700;
    letter-spacing: 1px;
    color: var(--green);
    white-space: nowrap;
  }

  /* Back */
  .card--back .person {
    position: absolute;
    right: 40px;
    top: 58px;
    text-align: right;
    font-family: "Roboto Slab", Georgia, serif;
    font-weight: 700;
    white-space: nowrap;
  }
  .person .person-name {
    font-size: 24px;
    color: var(--navy);
  }
  .person .person-role {
    font-size: 19px;
    color: var(--teal);
    margin-top: 2px;
  }
  .card--back .brand-name {
    position: absolute;
    left: 48px;
    top: 164px;
    font-size: 34px;
    font-weight: 700;
    color: var(--green);
    letter-spacing: -0.5px;
    white-space: nowrap;
  }
  .contact-list {
    position: absolute;
    left: 48px;
    top: 236px;
    list-style: none;
    font-size: 16px;
    color: var(--ink);
  }
  .contact-list li {
    display: flex;
    align-items: center;
    gap: 10px;
    height: 26px;
    white-space: nowrap;
  }
  .contact-list svg {
    width: 15px;
    height: 15px;
    flex: none;
  }
</style>
</head>
<body>
<main class="sheet">

  <section class="card card--front" aria-label="Card front">
    <div class="brand-name">Coastal Bright Sweep</div>
    <p class="slogan">Turning everyday waste into a fresh new start</p>
    <p class="services">EVENTS + COMMERCIAL + WASTE</p>
  </section>

  <section class="card card--back" aria-label="Card back">
    <div class="person">
      <div class="person-name">MORGAN ELLERY</div>
      <div class="person-role">CLIENT MANAGER</div>
    </div>
    <div class="brand-name">Coastal Bright Sweep</div>
    <ul class="contact-list">
      <li>
        <svg viewBox="0 0 16 16" aria-hidden="true"><rect x="4" y="1" width="8" height="14" rx="1.5" fill="none" stroke="var(--navy)" stroke-width="1.8"/><circle cx="8" cy="12.5" r="0.9" fill="var(--navy)"/></svg>
        <span>0400 318 256</span>
      </li>
      <li>
        <svg viewBox="0 0 16 16" aria-hidden="true"><rect x="1" y="3.5" width="14" height="9.5" fill="var(--navy)"/><path d="M1 3.5 L8 9 L15 3.5" fill="none" stroke="var(--paper)" stroke-width="1.2"/></svg>
        <span>mellery@coastalbrightsweep.com.au</span>
      </li>
      <li>
        <svg viewBox="0 0 16 16" aria-hidden="true"><circle cx="8" cy="8" r="7" fill="var(--navy)"/><path d="M1 8 H15 M8 1 C4.5 4 4.5 12 8 15 M8 1 C11.5 4 11.5 12 8 15" fill="none" stroke="var(--paper)" stroke-width="1"/></svg>
        <span>www.coastalbrightsweep.com.au</span>
      </li>
    </ul>
  </section>

</main>
</body>
</html>
```